International oil and gas consultancy needs a business card design

We need a business card design for a new oil and gas consultancy business based in Perth Australia. This is a professional services business and needs a moderately conservative type of business card. The business card also needs to be simple and uncluttered. The colour of the business logo is dark red (see attached file).
The front of the card should have a white background and mainly black lettering and perhaps some use of dark red and/or grey (your choice).
The back of the card should have a light grey background with dark red, black and or both dark red & black lettering (your choice).
Please find attached a clear brief of how I would like the business card designed.
Updates

Hello Everyone, I have slightly modified the brief. The main change is to incorporate some dark red and grey colours into the card, while still keeping the black lettering dominant. I have made the changes in the attached detailed brief document. Regards

Please note, the front of the card must say Harbor Ledger Advisory (in addition to the logo).

Industry/Entity Type

Conservative

Requirements
Must have
• brief has been updated. please refer to attachment for details.

Front of the card MUST say Harbor Ledger Advisory (in addition to the logo)

```html
<!DOCTYPE html>
<html lang="en">
<head>
<meta charset="utf-8">
<title>Harbor Ledger Advisory – Business Card</title>
<link href="https://fonts.googleapis.com/css2?family=Arimo:wght@400&display=swap" rel="stylesheet">
<style>
  :root {
    --page: #ffffff;
    --card-border: #6f6f6f;
    --ink: #111111;
    --brand-red: #9a1c22;
    --soft-grey: #ececec;
    --field-edge: #f4f4f4;
  }
  * { box-sizing: border-box; margin: 0; padding: 0; }
  html, body {
    width: 1200px; height: 1000px; overflow: hidden;
    background: var(--page);
    font-family: "Arimo", Arial, sans-serif;
    color: var(--ink);
  }
  .card {
    position: absolute;
    left: 147px; top: 234px;
    width: 928px; height: 546px;
    border: 1px solid var(--card-border);
    background: linear-gradient(215deg, #e9e9e9 0%, #f7f7f7 25%, #ffffff 45%, #ffffff 100%);
    overflow: hidden;
  }
  .brand {
    position: absolute;
    left: 18px; top: 62px;
    display: flex; align-items: center; gap: 16px;
  }
  .brand-square {
    width: 34px; height: 34px;
    background: var(--brand-red);
    flex: none;
  }
  .brand-name {
    font-size: 40px;
    line-height: 1.15;
    color: var(--brand-red);
    width: 320px;
  }
  .holder {
    position: absolute;
    right: 17px; top: 20px;
    text-align: right;
  }
  .holder-name { font-size: 38px; line-height: 42px; }
  .holder-role { font-size: 28px; margin-top: 28px; }
  .holder-company { font-size: 28px; margin-top: 38px; }
  .contacts {
    position: absolute;
    left: 390px; top: 303px;
    list-style: none;
  }
  .contact {
    display: flex; gap: 5px;
    height: 40px;
    margin-bottom: 22.5px;
  }
  .contact-icon {
    width: 40px; height: 40px;
    border: 3px solid var(--field-edge);
    background: #fff;
    display: flex; align-items: center; justify-content: center;
  }
  .contact-icon svg { width: 18px; height: 18px; }
  .contact-text {
    width: 491px; height: 40px;
    border: 3px solid var(--field-edge);
    background: linear-gradient(90deg, #ffffff 0%, #fafafa 50%, var(--soft-grey) 100%);
    font-size: 25px;
    display: flex; align-items: center; justify-content: center;
    white-space: nowrap;
  }
  .abn {
    position: absolute;
    left: 19px; bottom: 12px;
    font-size: 14px;
  }
</style>
</head>
<body>
  <div class="card">
    <div class="brand">
      <span class="brand-square"></span>
      <span class="brand-name">Harbor Ledger Advisory</span>
    </div>

    <div class="holder">
      <p class="holder-name">Dana Marlow</p>
      <p class="holder-role">Director</p>
      <p class="holder-company">Harbor Ledger Advisory</p>
    </div>

    <ul class="contacts">
      <li class="contact">
        <span class="contact-icon">
          <svg viewBox="0 0 18 18" fill="none" stroke="#9a1c22" stroke-width="1.8">
            <path d="M9 16 C5 11 4 9 4 7 a5 5 0 0 1 10 0 c0 2 -1 4 -5 9z"/>
            <circle cx="9" cy="7" r="1.6"/>
          </svg>
        </span>
        <span class="contact-text">Region: Australasia and South East Asia</span>
      </li>
      <li class="contact">
        <span class="contact-icon">
          <svg viewBox="0 0 18 18" fill="none" stroke="#9a1c22" stroke-width="1.6">
            <circle cx="9" cy="9" r="7.5"/>
            <path d="M6 5 l2 2 -1 1 c1 2 2 3 4 4 l1 -1 2 2 -1.5 1.2 C9 13.5 5 9.5 4.8 6.5z" fill="#9a1c22" stroke="none"/>
          </svg>
        </span>
        <span class="contact-text">Phone: +61&nbsp; (0)400 555 218</span>
      </li>
      <li class="contact">
        <span class="contact-icon">
          <svg viewBox="0 0 18 18" fill="none" stroke="#9a1c22" stroke-width="1.8">
            <rect x="1.5" y="4" width="15" height="10"/>
            <path d="M1.5 4 L9 10 L16.5 4 M1.5 14 L7 9 M16.5 14 L11 9"/>
          </svg>
        </span>
        <span class="contact-text">Email: dana@harborledger.com</span>
      </li>
      <li class="contact">
        <span class="contact-icon">
          <svg viewBox="0 0 18 18" fill="none" stroke="#9a1c22" stroke-width="1.5">
            <circle cx="8" cy="8" r="6.5"/>
            <ellipse cx="8" cy="8" rx="3" ry="6.5"/>
            <path d="M1.5 8 H14.5"/>
            <path d="M10 10 L16 12 L13.5 13 L15.5 16 L14 17 L12 14 L10.5 16z" fill="#9a1c22" stroke="none"/>
          </svg>
        </span>
        <span class="contact-text">Website: www.harborledger.com</span>
      </li>
    </ul>

    <p class="abn">ABN: 12 345 678 901</p>
  </div>
</body>
</html>
```